Ledgerwise Business Card Design

Business Card Design for new business called Ledgerwise focused on selling business software to small and medium size companies who have outgrown Tallymark. Similar companies would be Tallymark, Nuvo, CoreFlow. Also Dealharbor would be good to look at for additional ideas around look and feel.

Target Market(s)

Business to Business

Industry/Entity Type

Information Technology

Contact Information for Business Card

Standard Business Card Information

Font styles to use
Sans Serif

```html
<!DOCTYPE html>
<html lang="en">
<head>
<meta charset="utf-8">
<title>Ledgerwise Business Card</title>
<link rel="stylesheet" href="https://fonts.googleapis.com/css2?family=Arimo:wght@400;700&family=Tinos&display=swap">
<style>
  :root {
    --navy: #0f4c81;
    --orange: #e8872a;
    --paper: #f7f7f7;
    --backdrop: #e9e6e1;
    --line: #c9d6e4;
    --white: #ffffff;
  }
  * { margin: 0; padding: 0; box-sizing: border-box; }
  html, body { width: 1200px; height: 902px; overflow: hidden; }
  body {
    background: var(--backdrop);
    font-family: "Arimo", Arial, sans-serif;
    position: relative;
  }
  .card {
    position: absolute;
    left: 100px; top: 165px;
    width: 1000px; height: 571px;
    background: var(--paper);
    overflow: hidden;
    box-shadow: 0 10px 30px rgba(0,0,0,.18);
  }
  .card__band { position: absolute; inset: 0; }
  .brand {
    position: absolute;
    left: 0; right: 0; top: 150px;
    display: flex; align-items: center; justify-content: center; gap: 16px;
  }
  .brand__dot {
    width: 40px; height: 40px; border-radius: 50%;
    background: var(--orange);
  }
  .brand__name {
    font-weight: 700; font-size: 72px; letter-spacing: -1px;
    color: var(--navy);
  }
  .person {
    position: absolute; left: 130px; top: 430px;
    text-align: right; width: 240px;
  }
  .person__name {
    font-family: "Tinos", "Times New Roman", serif;
    font-size: 46px; color: var(--orange); line-height: 1;
  }
  .person__role {
    font-family: "Tinos", "Times New Roman", serif;
    font-size: 24px; color: var(--white); margin-top: 4px;
  }
  .divider {
    position: absolute; left: 410px; top: 380px;
    width: 2px; height: 150px; background: var(--line);
  }
  .contacts {
    position: absolute; left: 440px; top: 385px;
    list-style: none;
  }
  .contacts li {
    display: flex; align-items: center; gap: 14px;
    color: var(--white); font-size: 22px; height: 35px;
  }
  .contacts svg { width: 20px; height: 20px; flex: none; }
</style>
</head>
<body>
  <div class="card">
    <svg class="card__band" viewBox="0 0 1000 571" preserveAspectRatio="none" aria-hidden="true">
      <path d="M0,345 C320,390 720,280 1000,70 L1000,571 L0,571 Z" fill="var(--navy)"/>
    </svg>

    <div class="brand">
      <span class="brand__dot"></span>
      <span class="brand__name">Ledgerwise</span>
    </div>

    <div class="person">
      <div class="person__name">Mara Lind</div>
      <div class="person__role">Director</div>
    </div>

    <div class="divider"></div>

    <ul class="contacts">
      <li>
        <svg viewBox="0 0 20 20"><rect width="20" height="20" fill="var(--orange)"/><path d="M6 4l2.5 0 1 3-1.5 1.2a8 8 0 0 0 3.8 3.8L13 10.5l3 1V14a1.5 1.5 0 0 1-1.5 1.5A10.5 10.5 0 0 1 4.5 5.5 1.5 1.5 0 0 1 6 4z" fill="var(--white)"/></svg>
        0400 555 218
      </li>
      <li>
        <svg viewBox="0 0 20 20"><rect width="20" height="20" fill="var(--orange)"/><rect x="4" y="6" width="12" height="8" fill="none" stroke="var(--white)" stroke-width="1.5"/><path d="M4 6l6 5 6-5" fill="none" stroke="var(--white)" stroke-width="1.5"/></svg>
        hello@ledgerwise.com.au
      </li>
      <li>
        <svg viewBox="0 0 20 20"><rect width="20" height="20" fill="var(--orange)"/><circle cx="10" cy="10" r="5.5" fill="none" stroke="var(--white)" stroke-width="1.5"/><path d="M4.5 10h11M10 4.5c-2.5 3-2.5 8 0 11M10 4.5c2.5 3 2.5 8 0 11" fill="none" stroke="var(--white)" stroke-width="1.2"/></svg>
        www.Ledgerwise.com.au
      </li>
      <li>
        <svg viewBox="0 0 20 20"><rect width="20" height="20" fill="var(--orange)"/><path d="M10 16s-5-5-5-8.5a5 5 0 0 1 10 0C15 11 10 16 10 16z" fill="var(--white)"/><circle cx="10" cy="7.5" r="1.8" fill="var(--orange)"/></svg>
        PO Box 4410 Harbourview Qld 4870
      </li>
    </ul>
  </div>
</body>
</html>
```